Flyer Design for sewing business

Hi. i need flyers for my new business called " Telvo Designs". I am based in Sauchie. I offer Door to Door Clothing Alteration Service!
I provide a door to door alteration service for Clackmannanshire area with 20 miles radiance! (I give free consultations at your preferred location where I can accurately quote the cost of the alteration, as this depends on the garment itself. I aim to deliver the completed item back to you within a week though often it is less than this.)
I also design and sew occasional girls dresses ( first communion, flower girl, party dresses)
The consultation are free with no commitment to take the service.

I wold like see designs that use colors similar to colors on my website, like dusty pink, orange.

To contact either phone RUTH 07913284406
or email: ruth.marsk71@quillbox.com

www.pagebook.com/telvodesigns
www.telvo-designs.sitenest.com

THAT IS THE Price List Jeans/Trousers: Shorten....................................from £10.00 Taken in (waist).......................from £8.00 Taken in (side seams)..............from £10.00 Replace zip...............................from £10.00 Dresses/Skirts: Shorten....................................from £10.00 Taken in (waist).......................from £8.00 Taken in (side seams)..............from £8.00 Replace zip...............................from £10.00 Jacket/Coat: Shorten sleeves........................from £12.00 Shorten length (Jacket)...........from £16.00 Shorten length (Coat)..............from £18.00 Taken in (back seam)...............from £12.00 Taken in (side seams)..............from £18.00 Repairs......................................from £5.00 Bridal: Shorten Wedding Dress...........from £25.00 All other bridal alteration quotes can be given on consultation.

Reason: HI, ALL! IN THE NEXT FEW DAYS I GONE EXPERIENCE HOUSE MOVE AND SOME STRESS INVOLVING IN THIS.THANK YOU ALL FOR UNDERSTANDING AND A PATIENCE!

Industry/Entity Type

Business

```html
<!DOCTYPE html>
<html lang="en">
<head>
<meta charset="utf-8">
<title>Telvo Designs – Flyer</title>
<link rel="stylesheet" href="https://fonts.googleapis.com/css2?family=Roboto+Condensed:wght@300;700&family=Marcellus&family=Alice&display=swap">
<style>
  :root {
    --red: #ee3e33;
    --pink: #ef7fae;
    --pink-soft: #f2b3cc;
    --rose: #e79ab8;
    --cream: #f8e6e0;
    --paper: #fdfbf8;
    --ink: #1d1d1d;
    --blue: #2c5d9f;
    --backdrop: #e6d7da;
    --white: #ffffff;
  }
  * { box-sizing: border-box; margin: 0; padding: 0; }
  html, body { width: 1200px; height: 1134px; overflow: hidden; }
  body { background: var(--backdrop); position: relative; font-family: "Alice", serif; }

  .flyer { position: absolute; top: 172px; width: 560px; height: 790px; overflow: hidden; box-shadow: 0 6px 18px rgba(0,0,0,.18); }
  .flyer--front { left: 25px; background: var(--rose); }
  .flyer--back { left: 615px; background: var(--cream); }

  .footer-band { position: absolute; left: 0; bottom: 0; width: 100%; height: 62px; background: var(--red);
    display: flex; align-items: center; justify-content: center; gap: 10px; color: var(--white);
    font-family: "Alice", serif; font-weight: bold; font-size: 16px; }
  .footer-band .divider { width: 2px; height: 26px; background: var(--ink); }

  /* front */
  .headline-band { position: absolute; top: 0; left: 0; width: 100%; height: 292px; background: var(--red);
    color: var(--white); text-align: center; padding-top: 28px; font-family: "Roboto Condensed", sans-serif; }
  .headline-band .bold { font-weight: 700; font-size: 80px; line-height: 78px; }
  .headline-band .light { font-weight: 300; font-size: 62px; line-height: 76px; }
  .mannequin-photo { position: absolute; top: 292px; left: 0; width: 100%; height: 436px;
    background: linear-gradient(135deg, #d88aa8, #f0b8cc 45%, #e08fb0); }
  .info-card { position: absolute; top: 318px; left: 98px; width: 430px; height: 335px; background: var(--paper);
    transform: rotate(-4deg); box-shadow: 0 3px 10px rgba(0,0,0,.2); padding: 22px 26px 0 118px; }
  .info-card h2 { font-family: "Alice", serif; font-size: 22px; color: var(--ink); letter-spacing: .5px; margin-bottom: 8px; }
  .info-card p { font-size: 15.5px; line-height: 25px; color: var(--blue); text-align: center; margin-bottom: 14px; }
  .info-card .spaced { letter-spacing: 5px; }
  .dress-form-photo { position: absolute; top: 372px; left: 40px; width: 140px; height: 340px; border-radius: 40px 40px 10px 10px;
    background: linear-gradient(180deg, #f4eee6, #e6dbcd); }

  .name-box { position: absolute; background: var(--white); display: flex; align-items: center; justify-content: center;
    text-align: center; font-family: "Marcellus", serif; color: var(--ink); box-shadow: 0 2px 6px rgba(0,0,0,.2); }
  .name-box::before { content: ""; position: absolute; inset: 7px; border: 2px dashed var(--ink); }
  .name-box--front { top: 560px; left: 430px; width: 100px; height: 100px; font-size: 13px; transform: rotate(-4deg); }
  .name-box--back { top: 276px; left: 32px; width: 132px; height: 132px; font-size: 16px; transform: rotate(-4deg); }

  /* back */
  .dress-detail-photo { position: absolute; top: 0; left: 0; width: 100%; height: 262px;
    background: linear-gradient(160deg, #f58fbd, #f9bcd6 50%, #ee86b4); }
  .girl-dress-photo { position: absolute; top: 262px; left: 298px; width: 248px; height: 340px;
    background: linear-gradient(180deg, #c9b9a8, #f3eff0 55%, #e4d9d8); }
  .brand-text { position: absolute; top: 420px; left: 26px; width: 270px; text-align: center; }
  .brand-text h1 { font-family: "Marcellus", serif; font-weight: 400; color: var(--red); font-size: 40px; line-height: 42px; margin-bottom: 6px; }
  .brand-text .lead { color: var(--red); font-weight: bold; font-size: 19px; line-height: 22px; margin-bottom: 6px; }
  .brand-text .sub { color: var(--ink); font-weight: bold; font-size: 15px; line-height: 20px; }
  .thread-photo { position: absolute; top: 600px; left: 30px; width: 220px; height: 88px; border-radius: 50%;
    background: radial-gradient(ellipse, #b8a99a, #7c7a7c 70%); }
  .badge { position: absolute; top: 505px; left: 362px; width: 150px; height: 150px; }
  .badge-text { position: absolute; top: 520px; left: 362px; width: 150px; text-align: center; color: var(--white);
    font-family: "Roboto Condensed", sans-serif; }
  .badge-text .big { font-weight: 700; font-size: 36px; line-height: 36px; }
  .badge-text .mid { font-size: 21px; line-height: 24px; }
  .badge-text .small { font-family: "Alice", serif; color: var(--ink); font-size: 13px; line-height: 14px; margin-top: 4px; }
  .contact { position: absolute; top: 672px; left: 0; width: 100%; padding-left: 210px; color: var(--ink); font-weight: bold; font-size: 15px; line-height: 20px; }
  .contact .phone { color: var(--red); font-size: 22px; font-weight: normal; }
</style>
</head>
<body>

<section class="flyer flyer--front">
  <header class="headline-band">
    <div class="bold">Door to Door<br>Clothing</div>
    <div class="light">Alteration Service</div>
  </header>
  <div class="mannequin-photo" role="img" aria-label="Pink tulle fabric background"></div>
  <div class="info-card">
    <h2>Free Consultation</h2>
    <p>at your preferred location where I can accurately quote the cost of alteration, as this depends on the garment itself.</p>
    <p>My aim to deliver the completed item back to you within <span class="spaced">COMMITED</span> Period often it is less than this.</p>
  </div>
  <div class="dress-form-photo" role="img" aria-label="Dress form with tape measure and scissors"></div>
  <div class="name-box name-box--front">TELVO<br>DESIGNS</div>
  <footer class="footer-band">
    <span>www.pagebook.com/telvodesigns</span><span class="divider"></span><span>www.telvo-designs.sitenest.com</span>
  </footer>
</section>

<section class="flyer flyer--back">
  <div class="dress-detail-photo" role="img" aria-label="Close-up of pink satin dress sash with jewelled bow"></div>
  <div class="girl-dress-photo" role="img" aria-label="Girl in white tulle dress with pink sash"></div>
  <div class="name-box name-box--back">TELVO<br>DESIGNS</div>
  <div class="brand-text">
    <h1>TELVO<br>DESIGNS</h1>
    <p class="lead">I also design and sew occasional girls dresses.</p>
    <p class="sub">First communion, flower girl, party dresses</p>
  </div>
  <div class="thread-photo" role="img" aria-label="Spools of thread on a sewing table"></div>
  <svg class="badge" viewBox="0 0 150 150" aria-hidden="true"><circle cx="75" cy="75" r="74" fill="var(--pink)"/></svg>
  <div class="badge-text">
    <div class="big">FREE</div>
    <div class="mid">Consultation</div>
    <div class="small">No commitment<br>to take the<br>service</div>
  </div>
  <div class="contact">
    <div>Phone: RUTH <span class="phone">07913284406</span></div>
    <div>or email: ruth.marsk71@quillbox.com</div>
  </div>
  <footer class="footer-band">
    <span>www.pagebook.com/telvodesigns</span><span class="divider"></span><span>www.telvo-designs.sitenest.com</span>
  </footer>
</section>

</body>
</html>
```